K&R Security Services PTY. LTD.

Ive just had my logo made and I'm looking for some simple but strong designs for my business cards the company is a security company.

Please use dark colors.

Regards,

Owen Deloit

Reason: Need more time for discussion with other directors

Industry/Entity Type

Security

Font styles to use
Sans Serif
Decorative

```html
<!DOCTYPE html>
<html lang="en">
<head>
<meta charset="utf-8">
<title>K&amp;R Security Services — Business Card</title>
<link rel="stylesheet" href="https://fonts.googleapis.com/css2?family=Cinzel:wght@400;700&family=Quicksand:wght@400;500&display=swap">
<style>
  :root {
    --backdrop: #3b4447;
    --card: #ffffff;
    --ink: #1c1c1c;
    --ink-soft: #555a5c;
    --ink-faint: #7a7f81;
    --rule: #3a3a3a;
    --mark: #6f7a7c;
  }
  * { box-sizing: border-box; margin: 0; padding: 0; }
  html, body { width: 1200px; height: 741px; overflow: hidden; }
  body { background: var(--backdrop); position: relative; }

  .card {
    position: absolute;
    left: 399px;
    width: 409px;
    height: 236px;
    background: var(--card);
    color: var(--ink);
  }
  .card--front { top: 89px; }
  .card--back { top: 413px; }

  /* front */
  .brand-mark {
    position: absolute;
    left: 31px; top: 39px;
    width: 34px; height: 34px;
    background: var(--mark);
  }
  .holder-name {
    position: absolute;
    left: 74px; top: 41px;
    font-family: "Cinzel", serif;
    font-weight: 400;
    font-size: 24px;
    line-height: 30px;
    letter-spacing: 0.3px;
    color: var(--ink);
  }
  .divider {
    position: absolute;
    left: 30px; right: 31px; top: 174px;
    border: 0;
    border-top: 1px solid var(--rule);
  }
  .contact {
    position: absolute;
    top: 185px;
    font-family: "Quicksand", sans-serif;
    font-size: 9px;
    color: var(--ink-soft);
    list-style: none;
  }
  .contact li {
    display: flex; align-items: center; gap: 8px;
    height: 14px;
    white-space: nowrap;
  }
  .contact svg { width: 8px; height: 8px; fill: var(--ink); flex: none; }
  .contact--address { left: 29px; letter-spacing: 0.2px; }
  .contact--phones { left: 297px; font-size: 8px; color: var(--ink-faint); }
  .contact--phones li { gap: 10px; letter-spacing: 0.6px; }

  /* back */
  .back-mark {
    position: absolute;
    left: 50%; top: 56px;
    width: 96px; height: 96px;
    transform: translateX(-50%);
    border-radius: 50%;
    background: var(--mark);
  }
  .company-name {
    position: absolute;
    left: 0; right: 0; top: 177px;
    text-align: center;
    font-family: "Cinzel", serif;
    font-weight: 700;
    font-size: 10.5px;
    color: var(--ink);
  }
</style>
</head>
<body>

<section class="card card--front">
  <span class="brand-mark" role="img" aria-label="K&amp;R Security Services logo"></span>
  <h1 class="holder-name">Owen Deloit</h1>
  <hr class="divider">
  <ul class="contact contact--address">
    <li>
      <svg viewBox="0 0 10 10"><path d="M5 0a3.5 3.5 0 0 0-3.5 3.5C1.5 6 5 10 5 10s3.5-4 3.5-6.5A3.5 3.5 0 0 0 5 0zm0 5a1.5 1.5 0 1 1 0-3 1.5 1.5 0 0 1 0 3z"/></svg>
      <span>P.O. Box 7 Ashgrove Victoria 3170</span>
    </li>
    <li>
      <svg viewBox="0 0 10 10"><path d="M0 2h10v6H0z M0 2l5 3.5L10 2" fill="none" stroke="#1c1c1c" stroke-width="1.2"/></svg>
      <span>owen@deloit.net.au / K.R@deloit.net.au</span>
    </li>
  </ul>
  <ul class="contact contact--phones">
    <li>
      <svg viewBox="0 0 10 10"><path d="M3 0h4a1 1 0 0 1 1 1v8a1 1 0 0 1-1 1H3a1 1 0 0 1-1-1V1a1 1 0 0 1 1-1zm0 1.5v6h4v-6z"/></svg>
      <span>0400123456</span>
    </li>
    <li>
      <svg viewBox="0 0 10 10"><path d="M2 0l2 2.5-1 1.2a6 6 0 0 0 3.3 3.3l1.2-1L10 8l-1.5 2C4 10 0 6 0 1.5z"/></svg>
      <span>(03) 90001234</span>
    </li>
  </ul>
</section>

<section class="card card--back">
  <span class="back-mark" role="img" aria-label="K&amp;R Security Services logo"></span>
  <p class="company-name">K&amp;R Security Services Pty. Ltd.</p>
</section>

</body>
</html>
```